Design a Box for my Skin Care product

I need a beautiful design for my new skin care product.

I will need a design for the box, the 3 tubes that go inside the box and at the end I need a 3d of the box.

Details:
It will be a facial kit.
You need to add my logo( provided)
A box with a beautiful face would be apropriate

Measurements will be provided

Im attaching pictures of examples and logo

I need:
1 box design
3 tube design
3d version of the box

```html
<!DOCTYPE html>
<html lang="en">
<head>
<meta charset="utf-8">
<title>Coastal Fern Botanics – Natural Skin Care Box</title>
<link href="https://fonts.googleapis.com/css2?family=PT+Sans:wght@400;700&display=swap" rel="stylesheet">
<style>
  :root {
    --bg-light: #e6e6e6;
    --bg-dark: #c9c9c9;
    --panel-white: #ffffff;
    --leaf-green: #3f9a2a;
    --leaf-light: #8cc63f;
    --leaf-pale: #cfe8a8;
    --band-green: #2e8b2a;
    --band-deep: #1b6b1f;
    --skin-light: #f6e2d6;
    --skin-mid: #e2b59e;
    --skin-shade: #c98f76;
    --hair-dark: #6a5546;
  }
  * { margin: 0; padding: 0; box-sizing: border-box; }
  html, body {
    width: 1200px;
    height: 849px;
    overflow: hidden;
  }
  body {
    background: radial-gradient(ellipse at 50% 40%, var(--bg-light) 0%, var(--bg-dark) 100%);
    font-family: "PT Sans", Arial, sans-serif;
    position: relative;
  }
  .box-lid {
    position: absolute;
    left: 100px;
    top: 120px;
    width: 1000px;
    height: 610px;
    background: var(--panel-white);
    overflow: hidden;
    box-shadow: 0 10px 30px rgba(0,0,0,0.18);
  }
  .portrait-area {
    position: absolute;
    right: 0;
    top: 0;
    width: 620px;
    height: 390px;
    background:
      linear-gradient(to right, var(--panel-white) 0%, rgba(255,255,255,0) 38%),
      linear-gradient(to top, var(--panel-white) 0%, rgba(255,255,255,0) 30%),
      radial-gradient(ellipse 45% 40% at 55% 30%, var(--skin-light) 0%, rgba(246,226,214,0) 100%),
      radial-gradient(ellipse 40% 35% at 70% 70%, var(--skin-shade) 0%, rgba(201,143,118,0) 100%),
      radial-gradient(ellipse 30% 60% at 100% 20%, var(--hair-dark) 0%, rgba(106,85,70,0) 100%),
      linear-gradient(120deg, var(--skin-light) 10%, var(--skin-mid) 60%, var(--skin-shade) 100%);
  }
  .brand-band {
    position: absolute;
    right: 0;
    top: 400px;
    width: 560px;
    height: 120px;
    background: linear-gradient(90deg, var(--leaf-light) 0%, var(--band-green) 100%);
    display: flex;
    align-items: center;
    justify-content: flex-end;
    padding-right: 50px;
  }
  .leaf-cluster {
    position: absolute;
    left: -60px;
    top: 300px;
    width: 620px;
    height: 340px;
    background: radial-gradient(closest-side, var(--leaf-green) 0%, var(--leaf-light) 45%, rgba(207,232,168,0.7) 75%, rgba(255,255,255,0) 100%);
  }
  .base-strip {
    position: absolute;
    left: 0;
    bottom: 0;
    width: 100%;
    height: 40px;
    background: var(--band-deep);
  }
  .brand-mark {
    display: flex;
    align-items: center;
    gap: 10px;
    font-weight: 700;
    font-size: 30px;
    white-space: nowrap;
  }
  .brand-mark .dot {
    width: 16px;
    height: 16px;
    border-radius: 50%;
  }
  .brand-mark--header {
    position: absolute;
    left: 60px;
    top: 60px;
    color: var(--leaf-green);
  }
  .brand-mark--header .dot { background: var(--leaf-green); }
  .brand-mark--band { color: var(--panel-white); }
  .brand-mark--band .dot { background: var(--panel-white); }
  .product-title {
    position: absolute;
    left: 100px;
    top: 160px;
    color: var(--leaf-green);
  }
  .product-title .line-natural {
    display: block;
    font-size: 48px;
    font-weight: 700;
    color: var(--leaf-light);
  }
  .product-title .line-skincare {
    display: block;
    font-size: 34px;
    font-weight: 400;
    letter-spacing: 1px;
  }
</style>
</head>
<body>
  <section class="box-lid">
    <div class="portrait-area" role="img" aria-label="Photograph of a woman resting with eyes closed"></div>
    <div class="brand-band">
      <div class="brand-mark brand-mark--band"><span class="dot"></span>Coastal Fern Botanics</div>
    </div>
    <div class="leaf-cluster" role="img" aria-label="Illustration of fresh green leaves"></div>
    <div class="brand-mark brand-mark--header"><span class="dot"></span>Coastal Fern Botanics</div>
    <h1 class="product-title">
      <span class="line-natural">Natural</span>
      <span class="line-skincare">SKIN CARE</span>
    </h1>
    <div class="base-strip"></div>
  </section>
</body>
</html>
```